Audio-Visual & Video Communications Business Requires a Cutting-edge Business Card Design

LinkVessel is a new Audio-Visual & Video Communications company in Cape Town, South Africa that is looking for a cutting-edge business card design. We sell these products to the Corporate, Education & Hospitality markets and will also host an Online Shop for companies and individuals to purchase our products online.

We are already using the following two colours in our logo and draft website. Please incorporate these colours into the design. Please note that our website is still in the design stage if you need to visit it. Green #a0ce4e & Dark Grey #333333.
Updates

Hi,

Please note that I have uploaded our logo in an .eps format.

Target Market(s)

Corporate Companies, Education Institutions & Hospitality Markets

Industry/Entity Type

Business

Requirements
Nice to have
• It would be great if you could incorporate the services that we offer.

1. Consultation & Design
2. Project Management
3. Supply & Installation
4. Onsite Support Personal
5. Online Shop

```html
<!DOCTYPE html>
<html lang="en">
<head>
<meta charset="utf-8">
<title>LinkVessel Business Card</title>
<link rel="stylesheet" href="https://fonts.googleapis.com/css2?family=Open+Sans:wght@400;600;700&display=swap">
<style>
  :root {
    --brand-green: #a0ce4e;
    --brand-grey: #333333;
    --card-dark: #363636;
    --card-light: #ffffff;
    --page-bg: #5a5a5a;
    --text-light: #f2f2f2;
    --text-soft: #e0e0e0;
  }
  * { margin: 0; padding: 0; box-sizing: border-box; }
  html, body {
    width: 1200px;
    height: 960px;
    overflow: hidden;
    background: var(--page-bg);
    font-family: "Open Sans", sans-serif;
  }
  .stage {
    width: 1200px;
    height: 960px;
    display: flex;
    flex-direction: column;
    align-items: center;
    justify-content: center;
    gap: 60px;
  }
  .card {
    width: 560px;
    height: 320px;
    border-radius: 18px;
    position: relative;
    overflow: hidden;
    box-shadow: 0 6px 18px rgba(0, 0, 0, 0.35);
  }
  .card-front {
    background: var(--card-light);
    display: flex;
    align-items: center;
    justify-content: center;
    gap: 14px;
  }
  .brand-dot {
    width: 30px;
    height: 30px;
    border-radius: 50%;
    background: var(--brand-green);
  }
  .brand-name {
    font-size: 40px;
    font-weight: 700;
    color: var(--brand-green);
    letter-spacing: -0.5px;
  }
  .card-back {
    background: var(--card-dark);
    display: flex;
    align-items: center;
    padding: 0 48px;
    gap: 32px;
  }
  .back-brand {
    font-size: 20px;
    font-weight: 700;
    color: var(--text-light);
    min-width: 96px;
  }
  .contact .person-name {
    font-size: 24px;
    font-weight: 600;
    color: var(--text-light);
    line-height: 1.1;
  }
  .contact .person-role {
    font-size: 19px;
    color: var(--text-soft);
    margin-bottom: 18px;
  }
  .contact .detail {
    font-size: 16px;
    color: var(--text-soft);
    line-height: 1.4;
  }
</style>
</head>
<body>
  <main class="stage">
    <section class="card card-front" aria-label="Business card front">
      <span class="brand-dot"></span>
      <span class="brand-name">LinkVessel</span>
    </section>

    <section class="card card-back" aria-label="Business card back">
      <div class="back-brand">LinkVessel</div>
      <div class="contact">
        <p class="person-name">Daniel Reyes</p>
        <p class="person-role">Director</p>
        <p class="detail">mobile: 21 4870.3152</p>
        <p class="detail">daniel@linkvessel.com</p>
      </div>
    </section>
  </main>
</body>
</html>
```